Lorvika.no is a new website about pedagogical entrepreneurship. It's main target group is teachers. The Fjellmark Institute for Classroom Media and the Nordvik Agency for Schools and Study are leading the project.

The web page is meant to show examples of how different methods of entrepreneurship can be used pedagogical in a learning environment. The page will also support the user with examples of different teaching programs and other examples of best practice.

Pedagogical entrepreneurship is not about business and men in suits. It's a method for learning. The focus in the design should be on school, education and new ways of learning.

The final product should be motivating and engaging, but at the same time governmental and serious. We are not looking for something "flashy" and corporate-looking, but a moderate, task-focused and clean design that state quality.

We need designs for three pages:
1 - frontpage
2 - subpage ("Metoder og undervisningsopplegg")
3 - subpage ("Smått-VERK i Brekkelia")

The interaction design for these three pages will be uploaded as an attachment.

We would like you to find inspiration in the following websites:
- www.gryvekst.no
- www.lavrek.no
- www.tovandstudio.com
- www.kvp.no
(more will be added)

Please use the attached logo, and feel free to use this as an inspiration for the rest of the design.

Target Market(s)

Teachers

Industry/Entity Type

Education

Requirements
Must have
• * Header with: Logo. Main navigation. Utility navigation. Search box.
* Footer
Should not have
• Images of men in suits.
Very strong graphical elements that stands out too much (we want it clean).

```html
<!DOCTYPE html>
<html lang="en">
<head>
<meta charset="utf-8">
<title>Lorvika.no – Pedagogical entrepreneurship</title>
<link href="https://fonts.googleapis.com/css2?family=Arimo:wght@400;700&family=Roboto+Condensed:wght@700&family=Handlee&family=Ubuntu:wght@400;500;700&display=swap" rel="stylesheet">
<style>
:root{
  --lavender:#ebe8f3;
  --page:#faf8fb;
  --green:#8fae1b;
  --green-dark:#6f8a10;
  --green-text:#4f7a12;
  --ink:#111;
  --muted:#6b6b73;
  --frame:#7b7b7b;
  --line:#c9cfa8;
  --dark:#2d2d2d;
  --blue:#2a5e96;
}
*{box-sizing:border-box;margin:0;padding:0}
html,body{width:900px;height:1200px;overflow:hidden}
body{position:relative;background:var(--page);font-family:Arimo,Arial,sans-serif;color:var(--ink)}
.abs{position:absolute}
.band-top{left:0;top:0;width:900px;height:240px;background:var(--lavender)}
.band-mid{left:0;top:328px;width:900px;height:78px;background:var(--lavender)}
.band-foot{left:0;top:940px;width:900px;height:210px;background:var(--lavender)}
.band-dark{left:0;top:1148px;width:900px;height:34px;background:var(--dark)}
.copyright{left:0;top:1185px;width:900px;text-align:center;font-size:7.5px;font-weight:700}

.social-top{left:388px;top:14px;display:flex;gap:6px}
.dot{width:28px;height:24px;border-radius:50%;background:#c9c7cf}
.search{left:656px;top:24px;display:flex;gap:2px}
.search-field{width:110px;height:16px;border:1px solid #a9b86a;background:#fff}
.search-btn{width:48px;height:16px;background:var(--green);color:#fff;font-size:10px;text-align:center;line-height:16px}
.brand{left:98px;top:46px;display:flex;align-items:center;gap:14px}
.brand-mark{width:50px;height:50px;border-radius:50%;background:#4a8fc7}
.brand-name{font-family:Ubuntu,sans-serif;font-weight:700;font-size:34px;color:#3a8ccf;line-height:1}
.brand-tag{font-size:7px;color:#2c4f8a;margin-top:2px}
.main-nav{left:482px;top:72px;width:334px;height:19px;background:#9c9c9c;border-radius:3px;display:flex;align-items:center;font-size:11px;color:#fff}
.main-nav a{padding:0 8px;color:#fff;text-decoration:none}
.main-nav .active{background:var(--green);height:17px;line-height:17px;margin-left:3px;padding:0 6px}

.slider{left:100px;top:106px;width:718px;height:212px;background:var(--frame);box-shadow:0 4px 6px rgba(0,0,0,.3)}
.slider-inner{left:10px;top:8px;width:698px;height:194px;background:#f4f4f4}
.slide-tab{top:8px;width:30px;height:178px;background:#e3e3e3;border:1px solid #c8c8c8}
.slide-tab .label{position:absolute;left:7px;top:6px;writing-mode:vertical-rl;transform:rotate(180deg);font-family:"Roboto Condensed",sans-serif;font-weight:700;font-size:10px;color:#444;height:70px;text-align:right}
.slide-tab .num{position:absolute;bottom:4px;width:100%;text-align:center;font-family:Ubuntu,sans-serif;font-weight:700;font-size:20px;color:#111}
.slide-tab.current{background:#111;border-color:#111}
.slide-tab.current .label{color:#fff;height:118px;top:4px}
.slide-tab.current .num{color:#fff}
.slide-main{left:40px;top:8px;width:554px;height:178px;background:#fafafa;border:1px solid #ddd}
.slide-text{left:385px;top:48px;font-family:Handlee,cursive;font-size:22px;line-height:25px;color:#111}
.dots{left:12px;top:112px;display:flex;flex-direction:column;gap:3px}
.dots span{width:5px;height:5px;border-radius:50%;background:#333}
.dots span.off{background:#aaa}

.teaser{top:347px;font-size:10px;font-weight:700}
.teaser small{display:block;margin-top:6px;font-variant:small-caps;font-size:10px;color:var(--muted);font-weight:700;line-height:14px}

.meter{left:102px;top:440px;width:168px;height:138px;background:#dcdcdc}
.meter-title{left:10px;top:8px;font-family:Ubuntu,sans-serif;font-weight:700;font-size:10px;color:var(--blue);line-height:11px}
.meter-dial{left:34px;top:34px;width:106px;height:74px;border-radius:6px;background:linear-gradient(135deg,#c8cbd8,#e6e6e6 50%,#d8c8c8)}
.meter-link{left:0;top:116px;width:168px;text-align:center;font-size:8px;color:var(--blue);text-decoration:underline}

.box{background:#fff;border:1px solid var(--line);border-radius:8px}
.ribbon{background:linear-gradient(#a9c42e,#7f9c16);color:#fff;font-family:Ubuntu,sans-serif;font-weight:700;text-align:center}
.get-started{left:305px;top:437px;width:360px;height:173px}
.get-started .ribbon{left:70px;top:5px;width:214px;height:22px;line-height:22px;font-size:12px}
.list{top:38px;width:144px;font-size:8px}
.list h3{font-size:8px;font-weight:400;color:var(--green-text);background:linear-gradient(#fff,#eee);padding:2px 4px 3px 16px;position:relative}
.list h3::before{content:"";position:absolute;left:4px;top:3px;width:8px;height:7px;background:var(--green);border-radius:2px}
.list li{list-style:none;border-bottom:1px dotted #555;padding:6px 0 5px 16px;position:relative}
.list li::before{content:"»";position:absolute;left:4px;font-weight:700}

.newsletter{left:677px;top:437px;width:168px;height:75px}
.side-title{font-family:Ubuntu,sans-serif;font-weight:500;font-size:11px;color:var(--green-text)}
.newsletter .side-title{left:8px;top:9px}
.newsletter p{left:8px;top:24px;width:154px;font-size:7.5px;line-height:11px}
.nl-field{left:8px;top:50px;width:100px;height:14px;border:1px solid #bbb;font-size:7.5px;color:#888;padding:2px 4px}
.nl-btn{left:112px;top:50px;width:46px;height:14px;background:var(--green);color:#fff;font-size:8px;text-align:center;line-height:14px}
.support{left:677px;top:543px;width:168px;height:67px}
.support .side-title{left:7px;top:8px}
.support p{left:58px;top:24px;width:102px;font-size:7.5px;line-height:10px}
.support svg{left:6px;top:20px}

.insp-tab{left:123px;top:644px;width:168px;height:21px;line-height:21px;font-size:10px;border-radius:3px 3px 0 0}
.inspirations{left:103px;top:665px;width:498px;height:202px;border-radius:12px}
.insp-item{left:5px;width:480px;height:54px}
.insp-photo{left:0;top:0;width:102px;height:52px;background:linear-gradient(#c9d1dc,#b8a6a0 55%,#e4e4e8)}
.insp-item h4{left:111px;top:0;font-size:9.5px;font-weight:400}
.insp-item p{left:111px;top:16px;width:372px;font-size:8.5px;line-height:16px;font-style:italic;color:var(--green-text)}
.locate{left:651px;top:665px;width:195px;height:156px;border:1px solid #bbb;background:#fff}
.locate .ribbon{left:0;top:0;width:195px;height:22px;line-height:22px;text-align:left;padding-left:8px;font-size:11px;font-variant:small-caps}
.map{left:5px;top:26px;width:184px;height:124px;background:linear-gradient(135deg,#e8e4da,#d9dccf 50%,#ecd9a8)}

.foot-col h5{font-family:Ubuntu,sans-serif;font-variant:small-caps;font-size:11px;font-weight:500;letter-spacing:.3px;margin-bottom:10px}
.foot-col a{display:block;font-size:9px;color:#555;text-decoration:underline;line-height:14px;margin-bottom:2px}
.foot-col a.caps{font-variant:small-caps;font-weight:700;font-size:10px}
.contact h5{font-family:Ubuntu,sans-serif;font-size:15px;font-weight:400;margin-bottom:8px}
.field{width:178px;height:22px;border:1px solid #ddd;background:#f6f5f8;border-radius:4px;font-size:10px;padding:4px 12px;margin-bottom:2px}
.field.area{height:58px}
.send{left:612px;top:1112px;width:56px;height:18px;background:#111;color:#fff;border-radius:6px;font-size:10px;text-align:center;line-height:18px}
.foot-brand{left:112px;top:1094px;display:flex;align-items:center}
.foot-brand .brand-mark{width:46px;height:46px}
.foot-social{left:352px;top:1108px;display:flex;gap:6px}
.foot-social span{width:32px;height:28px;border-radius:50%;background:#bdbbc2}
</style>
</head>
<body>
<div class="abs band-top"></div>
<div class="abs band-mid"></div>
<div class="abs band-foot"></div>
<div class="abs band-dark"></div>
<div class="abs copyright">© Copyright 2012 - lorvika.no</div>

<header>
  <div class="abs social-top"><span class="dot"></span><span class="dot"></span><span class="dot"></span></div>
  <div class="abs search"><div class="search-field"></div><div class="search-btn">Search</div></div>
  <div class="abs brand">
    <div class="brand-mark"></div>
    <div><div class="brand-name">Lorvika</div><div class="brand-tag">Entreprenørielle metoder i undervisningen</div></div>
  </div>
  <nav class="abs main-nav"><a class="active">Lorvikameter</a><a>Best practice schools</a><a>About lorvika.no</a></nav>
</header>

<section class="abs slider">
  <div class="abs slider-inner">
    <div class="abs slide-tab current" style="left:2px"><div class="label">Welcome to LORVIKA.no</div><div class="num">1</div></div>
    <div class="abs slide-main">
      <svg class="abs" style="left:0;top:14px" width="10" height="14"><path d="M0 0L9 7L0 14Z" fill="#111"/></svg>
      <div class="abs slide-text">A Great<br>&nbsp;&nbsp;&nbsp;Source<br>&nbsp;&nbsp;&nbsp;&nbsp;&nbsp;&nbsp;&nbsp;&nbsp;of........</div>
    </div>
    <div class="abs slide-tab" style="left:596px"><div class="label">LOREM IPSUM</div><div class="num">2</div></div>
    <div class="abs slide-tab" style="left:628px"><div class="label">LOREM IPSUM</div><div class="abs dots"><span></span><span></span><span class="off"></span></div><div class="num">3</div></div>
    <div class="abs slide-tab" style="left:660px"><div class="label">LOREM IPSUM</div><div class="num">4</div></div>
  </div>
</section>

<div class="abs teaser" style="left:143px">Learn About what, why and how!<small>What is pedagocical<br>entrepreneurship?</small></div>
<div class="abs teaser" style="left:422px">Plan your lessons!<small>Methods and teaching plans</small></div>
<div class="abs teaser" style="left:650px;top:343px">Be inspired!<small>Good examples / best practice</small></div>

<aside class="abs meter">
  <div class="abs meter-title">Are you working<br>entrepreneurship-like?</div>
  <div class="abs meter-dial" role="img" aria-label="Gauge illustration showing an entrepreneurship score"></div>
  <div class="abs meter-link">Try the lorvikameter!</div>
</aside>

<section class="abs box get-started">
  <div class="abs ribbon">Get started</div>
  <ul class="abs list" style="left:12px"><h3>Methods</h3><li>Leadership Team</li><li>Board Members</li><li>Client Testimonials</li><li>Our Partners</li><li>Why Choose Us?</li></ul>
  <ul class="abs list" style="left:204px"><h3>Teaching plans</h3><li>Leadership Team</li><li>Board Members</li><li>Client Testimonials</li><li>Our Partners</li><li>Why Choose Us?</li></ul>
</section>

<aside class="abs box newsletter">
  <div class="abs side-title">Newsletter Signup</div>
  <p class="abs">Sign up for our newsletter to receive the latest news and event postings.</p>
  <div class="abs nl-field">mail@example.com</div>
  <div class="abs nl-btn">Sign Up!</div>
</aside>
<aside class="abs box support">
  <div class="abs side-title">24/7 Technical Support</div>
  <svg class="abs" width="44" height="42" viewBox="0 0 44 42"><path d="M8 22a14 14 0 0 1 28 0" fill="none" stroke="#333" stroke-width="3"/><rect x="4" y="20" width="8" height="14" rx="3" fill="#333"/><rect x="32" y="20" width="8" height="14" rx="3" fill="#333"/><path d="M10 34q4 6 12 6" fill="none" stroke="#333" stroke-width="2"/></svg>
  <p class="abs">Integer ut quam velit susque blandit ante sit amet arcu.</p>
</aside>

<div class="abs ribbon insp-tab">ISPIRATIONS</div>
<section class="abs box inspirations">
  <article class="abs insp-item" style="top:14px"><div class="abs insp-photo" role="img" aria-label="Photo of a school building in winter"></div><h4 class="abs">Smått-VERK at Brekkelia school</h4><p class="abs">Nam condimentum eros quis ante lacinia tincidunt. Nulla facilisid magna nibh vehicula vitae laoreet vel posuere in ligula. Sed quis odio leo at sagittis orci.</p></article>
  <article class="abs insp-item" style="top:76px"><div class="abs insp-photo" role="img" aria-label="Photo of a school building in winter"></div><h4 class="abs">Smått-VERK at Brekkelia school</h4><p class="abs">Nam condimentum eros quis ante lacinia tincidunt. Nulla facilisid magna nibh vehicula vitae laoreet vel posuere in ligula. Sed quis odio leo at sagittis orci.</p></article>
  <article class="abs insp-item" style="top:137px"><div class="abs insp-photo" role="img" aria-label="Photo of a school building in winter"></div><h4 class="abs">Smått-VERK at Brekkelia school</h4><p class="abs">Nam condimentum eros quis ante lacinia tincidunt. Nulla facilisid magna nibh vehicula vitae laoreet vel posuere in ligula. Sed quis odio leo at sagittis orci.</p></article>
</section>

<aside class="abs locate">
  <div class="abs ribbon">Locate Us</div>
  <div class="abs map" role="img" aria-label="Street map showing the office location"></div>
</aside>

<footer>
  <div class="abs foot-col" style="left:117px;top:972px"><h5>Pedagocical entrepreneurship</h5><a class="caps">What is pedagocical<br>entrepreneurship?</a><a>Science</a><a>Best practice schools</a></div>
  <div class="abs foot-col" style="left:365px;top:972px"><h5>Gode eksempler</h5><a>Smått-VERK at Brekkelia school</a><a>Smått-VERK at Brekkelia school</a><a>Smått-VERK at Brekkelia school</a><a>See more....</a></div>
  <div class="abs contact" style="left:605px;top:972px"><h5>Contact Us</h5><div class="field">name</div><div class="field">email</div><div class="field area">message</div></div>
  <div class="abs send">send</div>
  <div class="abs foot-brand"><div class="brand-mark"></div></div>
  <div class="abs foot-social"><span></span><span></span><span></span><span></span><span></span></div>
</footer>
</body>
</html>
```